quiet meadow therapy (QMT)

I need to build a website for my therapy business.
There are two parts to the website
on the landing page; they choose whether they are therapists making a referral or patients needing more information.
After that, they are taken to their respective pages.
There is the textual information and a referral form on the therapist page, and on the patient page, the text is a bit different, and there will be a booking page on the patient page.
Visually minimal, it's a therapeutic website. I want it clean, clinical, and modern
colors: greenish blue or maybe orangish
PHP/html code
Updates

Hi everyone
I'm very sorry for the lack of responses to your designs. I am trying to work it out, but this platform has been a challenge for me.
I appreciate everyone's efforts, and I am unsure how to rate designs and move forward with the ones I like. There is a 5-star rating, but I don't understand how I'm supposed to politely say that it is not it without feeling like I'm going to affect someone's future rating negatively.
Please understand me. Thank you

Designs look the same

Target Market(s)

therapy and stress management

Industry/Entity Type

stress management therapy

Coding

Coded - Design and coding required

Number of Pages Required

5+ page

Font styles to use
Serif

Colors
0094D4
00A9DD
6FCCEA
C7EBF8
E9F6FB
00AB8E
00BBA5
67D7C9
C6EFE9
E9F9F6

Requirements
Must have
• landing page that that have 2 options. one for therapist another for patient

```html
<!DOCTYPE html>
<html lang="en">
<head>
<meta charset="utf-8">
<title>QMT — Quiet Meadow Therapy</title>
<link rel="stylesheet" href="https://fonts.googleapis.com/css2?family=Abril+Fatface&family=PT+Serif:wght@400;700&family=Poppins:wght@400;500;600&display=swap">
<style>
:root{
  --page:#e9ebed;
  --teal:#1fa382;
  --teal-dark:#138a6e;
  --teal-light:#67c2b3;
  --mint:#c6efe9;
  --ink:#111;
  --text:#444;
  --white:#fff;
  --star:#f5a623;
  --line:#d9dddf;
  --serif-display:"Abril Fatface",serif;
  --serif:"PT Serif",serif;
  --sans:"Poppins",sans-serif;
}
*{box-sizing:border-box;margin:0;padding:0}
html,body{width:1200px;height:4724px;overflow:hidden}
body{background:var(--page);position:relative;font-family:var(--serif);color:var(--text)}
.section{position:absolute;left:29px;width:1140px;overflow:hidden}
.photo{position:absolute;inset:0}

/* header */
.logo{position:absolute;display:flex;align-items:center;gap:12px;font-family:var(--sans);font-weight:500;font-size:44px;letter-spacing:12px;color:var(--ink)}
.logo-mark{width:34px;height:34px;border-radius:50%;background:var(--teal)}
.nav{position:absolute;width:540px;height:22px;list-style:none;font-family:var(--sans);font-size:15px;line-height:22px;color:var(--ink)}
.nav li{position:absolute;top:0;white-space:nowrap}
.nav li:nth-child(1){left:0}
.nav li:nth-child(2){left:83px}
.nav li:nth-child(3){left:167px}
.nav li:nth-child(4){left:264px}
.nav li:nth-child(5){left:358px}
.nav li:nth-child(6){left:475px}
.phone{position:absolute;display:flex;align-items:center;gap:10px;font-family:var(--sans);font-size:17px;color:var(--ink);white-space:nowrap}
.phone-icon{width:40px;height:40px;border-radius:50%;background:var(--teal);display:flex;align-items:center;justify-content:center}
.on-dark .logo,.on-dark .nav,.on-dark .phone{color:var(--white)}

.btn{position:absolute;display:flex;align-items:center;justify-content:center;font-family:var(--serif);font-weight:700;font-size:16px;letter-spacing:.5px;text-transform:uppercase}
.btn-teal{background:var(--teal);color:var(--white)}
.btn-white{background:var(--white);color:var(--teal)}

/* landing */
.landing{top:59px;height:649px}
.landing .photo{background:linear-gradient(100deg,#6b5a4c 0%,#b8ab9a 22%,#e8e2d8 45%,#d7d0c4 60%,#5d7896 78%,#3f4e63 100%)}
.menu-box{position:absolute;right:0;top:0;width:60px;height:37px;background:#444}
.landing-circle{position:absolute;left:322px;top:120px;width:300px;height:300px;border-radius:50%;background:rgba(180,228,214,.6)}
.landing-title{position:absolute;left:0;width:1140px;text-align:center;font-family:var(--serif-display);font-weight:400;line-height:1}
.landing-title .kicker{display:block;font-size:62px;color:var(--teal);margin-top:180px}
.landing-title .name{display:block;font-size:128px;color:var(--ink);margin-top:14px}

/* intro hero */
.intro{top:768px;height:652px}
.intro .photo{background:linear-gradient(180deg,#2f6f93 0%,#6f9bb5 30%,#c59a7c 62%,#d8642c 82%,#5a2a1a 100%)}
.intro-title{position:absolute;left:95px;top:150px;font-family:var(--serif-display);font-weight:400;font-size:56px;line-height:66px;color:var(--white);text-transform:uppercase}
.intro-text{position:absolute;left:95px;top:372px;width:480px;font-family:var(--sans);font-size:13px;line-height:19px;color:var(--white)}

/* about */
.about{top:1420px;height:623px;background:var(--white)}
.about-back{position:absolute;left:92px;top:84px;width:453px;height:422px;border-radius:24px;background:linear-gradient(180deg,var(--teal),#0f7d65)}
.about-photo{position:absolute;left:116px;top:106px;width:453px;height:413px;border-radius:24px;background:linear-gradient(135deg,#d9d6d0,#8f9a84 55%,#55684a)}
.eyebrow{font-family:var(--serif);font-weight:700;font-size:22px;color:var(--teal);text-transform:uppercase}
.about .eyebrow{position:absolute;left:629px;top:86px}
.about-name{position:absolute;left:629px;top:118px;font-family:var(--serif-display);font-weight:400;font-size:84px;line-height:1;color:var(--ink)}
.about-text{position:absolute;left:629px;top:220px;width:420px;font-size:13.5px;line-height:24.5px;text-align:justify;color:#555}

/* mission */
.mission{top:2043px;height:455px}
.mission .photo{background:linear-gradient(90deg,#1a93a0 0%,#2aa6ad 40%,#8fc8c6 58%,#d6d2cc 72%,#c2b6a8 100%)}
.mission-title{position:absolute;left:94px;top:78px;font-family:var(--serif-display);font-weight:400;font-size:32px;color:var(--white);text-transform:uppercase}
.mission-text{position:absolute;left:94px;top:132px;width:455px;font-size:14.5px;line-height:24px;font-weight:700;color:var(--white);text-align:justify}
.mission .btn{color:var(--ink);font-weight:400}

/* services */
.services{top:2498px;height:693px}
.services .photo{background:linear-gradient(180deg,#f1f2f3 0%,#e4e6e8 50%,#eef0f1 100%)}
.section-title{position:absolute;left:0;width:1140px;text-align:center;font-family:var(--serif-display);font-weight:400;font-size:28px;color:var(--teal);text-transform:uppercase}
.drop{position:absolute;width:212px;height:272px}
.drop svg{position:absolute;inset:0}
.drop-label{position:absolute;left:0;width:212px;top:188px;text-align:center;font-weight:700;font-size:18px;color:var(--white)}

/* values */
.values{top:3191px;height:453px}
.values .photo{background:linear-gradient(180deg,#2b3136 0%,#47525a 45%,#1c2a33 75%,#121a20 100%)}
.values .section-title{color:var(--white);top:96px;font-size:32px}
.values-sub{position:absolute;left:0;width:1140px;top:150px;text-align:center;font-weight:700;font-size:28px;color:var(--white)}
.values-text{position:absolute;left:200px;width:740px;top:200px;text-align:center;font-size:14px;line-height:24px;color:var(--white)}

/* reviews */
.reviews{top:3644px;height:631px;background:var(--white)}
.reviews .section-title{top:68px}
.rating{position:absolute;left:0;width:1140px;top:108px;text-align:center;font-weight:700;font-size:15px;color:var(--ink)}
.rating .stars{color:var(--star);letter-spacing:3px;margin-right:14px}
.halo{position:absolute;border-radius:50%;background:rgba(103,194,179,.09)}
.review{position:absolute;top:160px;width:295px;height:272px;border:2px solid var(--line);border-radius:18px;background:rgba(255,255,255,.6)}
.quote{position:absolute;left:20px;top:16px;font-family:var(--serif-display);font-size:56px;line-height:1;color:var(--ink)}
.review-text{position:absolute;left:20px;top:72px;width:258px;font-size:13px;line-height:21px;color:#555}
.review .stars{position:absolute;left:20px;top:188px;color:var(--star);font-size:17px;letter-spacing:3px}
.reviewer{position:absolute;left:20px;top:212px;font-weight:700;font-size:18px;letter-spacing:4px;color:var(--ink)}
.avatar{position:absolute;left:188px;top:226px;width:72px;height:72px;border-radius:50%;background:linear-gradient(135deg,#c9b9a8,#6f5a4b);border:3px solid var(--white)}
.btn-pill{border-radius:26px;font-size:17px;text-transform:none}

/* footer */
.footer{top:4275px;height:394px;background:#000;color:var(--white)}
.footer .logo{color:var(--white);left:92px;top:48px}
.footer-heading{position:absolute;font-family:var(--serif);font-weight:700;font-size:17px;color:var(--white);text-transform:uppercase}
.footer-note{position:absolute;left:92px;top:186px;font-family:var(--sans);font-size:14px;line-height:20px}
.subscribe{position:absolute;left:92px;top:241px;width:277px;height:42px;border:1px solid var(--white);display:flex;align-items:center;justify-content:space-between;padding:0 12px;font-family:var(--sans);font-size:11px}
.links{position:absolute;list-style:none;font-family:var(--sans);font-size:14px}
.quick li{height:25px}
.help li{height:31px}
.contact-item{position:absolute;left:841px;display:flex;align-items:center;gap:16px;font-family:var(--sans);font-size:13px;line-height:20px}
.ring{flex:none;width:30px;height:30px;border:1.5px solid var(--white);border-radius:50%;display:flex;align-items:center;justify-content:center}
.rule{position:absolute;left:106px;top:317px;width:927px;height:1px;background:#777}
.copyright{position:absolute;left:0;width:1140px;top:340px;text-align:center;font-family:var(--sans);font-size:14px}
</style>
</head>
<body>

<!-- landing: choose path -->
<section class="section landing">
  <div class="photo" role="img" aria-label="Photo of a therapist listening to a client on a sofa in a bright living room"></div>
  <div class="landing-circle"></div>
  <div class="menu-box"></div>
  <div class="logo" style="left:86px;top:20px"><span class="logo-mark"></span>QMT</div>
  <ul class="nav" style="left:303px;top:30px"><li>Home</li><li>About</li><li>Services</li><li>Mission</li><li>Resources</li><li>Contact</li></ul>
  <div class="phone" style="left:858px;top:20px"><span class="phone-icon"><svg width="18" height="18" viewBox="0 0 24 24"><path fill="#fff" d="M6.6 10.8a15 15 0 0 0 6.6 6.6l2.2-2.2c.3-.3.7-.4 1-.2 1.1.4 2.3.6 3.6.6.6 0 1 .4 1 1V20c0 .6-.4 1-1 1A17 17 0 0 1 3 4c0-.6.4-1 1-1h3.5c.6 0 1 .4 1 1 0 1.3.2 2.5.6 3.6.1.3 0 .7-.2 1z"/></svg></span>+1 555-014-2290</div>
  <h1 class="landing-title"><span class="kicker">WELCOME TO</span><span class="name">QMT</span></h1>
  <a class="btn btn-teal" style="left:325px;top:409px;width:211px;height:48px">Therapists</a>
  <a class="btn btn-white" style="left:576px;top:409px;width:209px;height:48px">Patients</a>
</section>

<!-- intro hero -->
<section class="section intro on-dark">
  <div class="photo" role="img" aria-label="Double exposure of a woman's profile against a blue and orange sunset sky"></div>
  <div class="logo" style="left:78px;top:18px"><span class="logo-mark"></span>QMT</div>
  <ul class="nav" style="left:303px;top:32px"><li>Home</li><li>About</li><li>Services</li><li>Mission</li><li>Resources</li><li>Contact</li></ul>
  <div class="phone" style="left:858px;top:22px"><span class="phone-icon"><svg width="18" height="18" viewBox="0 0 24 24"><path fill="#fff" d="M6.6 10.8a15 15 0 0 0 6.6 6.6l2.2-2.2c.3-.3.7-.4 1-.2 1.1.4 2.3.6 3.6.6.6 0 1 .4 1 1V20c0 .6-.4 1-1 1A17 17 0 0 1 3 4c0-.6.4-1 1-1h3.5c.6 0 1 .4 1 1 0 1.3.2 2.5.6 3.6.1.3 0 .7-.2 1z"/></svg></span>+1 555-014-2290</div>
  <h2 class="intro-title">Welcome to<br>Quiet Meadow<br>Therapy</h2>
  <p class="intro-text">Lorem ipsum dolor sit amet, consectetur adipiscing elit, sed do eiusmod tempor incididunt ut labore et dolore magna aliqua. exercitation ullamco laboris nisi ut aliquip ex ea commodo consequat.</p>
  <a class="btn btn-teal" style="left:95px;top:460px;width:211px;height:50px">Get Started</a>
</section>

<!-- about -->
<section class="section about">
  <div class="about-back"></div>
  <div class="about-photo" role="img" aria-label="Photo of a man talking with a woman holding a clipboard in a therapy room"></div>
  <p class="eyebrow">About Us</p>
  <h2 class="about-name">QMT</h2>
  <p class="about-text">Sed ut perspiciatis unde omnis iste natus error sit voluptatem accusantium doloremque laudantium, totam rem aperiam, eaque ipsa quae ab illo inventore veritatis et quasi architecto beatae vitae dicta sunt explicabo. Nemo enim ipsam voluptatem quia voluptas sit aspernatur aut odit aut fugit, sed quia consequuntur magni dolores eos qui ratione voluptatem sequi nesciunt. Neque porro quisquam est, qui dolorem ipsum quia dolor sit amet, consectetur, adipisci velit, sed quia non numquam eius modi tempora</p>
  <a class="btn btn-teal" style="left:629px;top:466px;width:145px;height:46px;font-weight:400;font-size:15px">Read More</a>
</section>

<!-- mission -->
<section class="section mission">
  <div class="photo" role="img" aria-label="Teal wash fading into a photo of a woman speaking on a sofa by a window"></div>
  <h2 class="mission-title">Mission Statement</h2>
  <p class="mission-text">Lorem ipsum dolor sit amet, consectetur adipiscing elit, sed do eiusmod tempor incididunt ut labore et dolore magna aliqua. Ut enim ad minim veniam, quis nostrud exercitation ullamco laboris nisi ut aliquip ex ea commodo consequat. Duis aute irure dolor in reprehenderit in voluptate velit esse cillum dolore eu fugiat nulla pariatur.</p>
  <a class="btn btn-white" style="left:94px;top:312px;width:147px;height:46px;font-size:15px">Learn More</a>
</section>

<!-- services -->
<section class="section services">
  <div class="photo" role="img" aria-label="Faint misty lake and mountain landscape"></div>
  <svg width="0" height="0" style="position:absolute">
    <defs>
      <linearGradient id="dropSplit" x1="0" y1="0" x2="1" y2="1">
        <stop offset="0" stop-color="#1fa98b"/><stop offset=".5" stop-color="#1fa98b"/>
        <stop offset=".5" stop-color="#67bcae"/><stop offset="1" stop-color="#67bcae"/>
      </linearGradient>
      <path id="dropShape" d="M106 0C150 62 212 100 212 166A106 106 0 0 1 0 166C0 100 62 62 106 0Z"/>
    </defs>
  </svg>
  <h2 class="section-title" style="top:76px">Our Services</h2>
  <div class="drop" style="left:98px;top:121px"><svg viewBox="0 0 212 272"><use href="#dropShape" fill="url(#dropSplit)"/></svg><span class="drop-label">Lorem ipsum</span></div>
  <div class="drop" style="left:338px;top:121px"><svg viewBox="0 0 212 272"><use href="#dropShape" fill="#1aa98b"/></svg><span class="drop-label">Lorem ipsum</span></div>
  <div class="drop" style="left:580px;top:121px"><svg viewBox="0 0 212 272"><use href="#dropShape" fill="url(#dropSplit)"/></svg><span class="drop-label">Lorem ipsum</span></div>
  <div class="drop" style="left:821px;top:121px"><svg viewBox="0 0 212 272"><use href="#dropShape" fill="url(#dropSplit)"/></svg><span class="drop-label">Lorem ipsum</span></div>
  <div class="drop" style="left:211px;top:329px"><svg viewBox="0 0 212 272"><use href="#dropShape" fill="url(#dropSplit)"/></svg><span class="drop-label">Lorem ipsum</span></div>
  <div class="drop" style="left:454px;top:329px"><svg viewBox="0 0 212 272"><use href="#dropShape" fill="url(#dropSplit)"/></svg><span class="drop-label">Lorem ipsum</span></div>
  <div class="drop" style="left:694px;top:329px"><svg viewBox="0 0 212 272"><use href="#dropShape" fill="url(#dropSplit)"/></svg><span class="drop-label">Lorem ipsum</span></div>
</section>

<!-- values -->
<section class="section values">
  <div class="photo" role="img" aria-label="Dim harbour city skyline at dusk"></div>
  <h2 class="section-title">Our Values</h2>
  <p class="values-sub">Seeks to prevent and treat mental health problems</p>
  <p class="values-text">Lorem ipsum dolor sit amet, consectetur adipiscing elit, sed do eiusmod tempor incididunt ut labore et dolore magna aliqua. Ut enim ad minim veniam, quis nostrud exercitation ullamco laboris nisi ut aliquip ex ea commodo consequat. fugiat nulla pariatur.</p>
  <a class="btn btn-teal" style="left:488px;top:292px;width:164px;height:48px;font-weight:400;font-size:15px">Contact Us</a>
</section>

<!-- reviews -->
<section class="section reviews">
  <div class="halo" style="left:380px;top:150px;width:300px;height:300px"></div>
  <div class="halo" style="left:470px;top:150px;width:300px;height:300px"></div>
  <h2 class="section-title">Real Reviews From Clients</h2>
  <p class="rating"><span class="stars">★★★★★</span>Rated 4.5 Stars. 153 Reviews</p>

  <article class="review" style="left:95px">
    <span class="quote">“</span>
    <p class="review-text">Lorem ipsum dolor sit amet, consectetur adipiscing elit, sed do eiusmod tempor incididunt ut labore et dolore magna aliqua. Ut enim ad minim veniam, quis nostrud</p>
    <span class="stars">★★★★★</span>
    <p class="reviewer">Jhone Deo</p>
    <span class="avatar" role="img" aria-label="Client portrait"></span>
  </article>
  <article class="review" style="left:422px">
    <span class="quote">“</span>
    <p class="review-text">Lorem ipsum dolor sit amet, consectetur adipiscing elit, sed do eiusmod tempor incididunt ut labore et dolore magna aliqua. Ut enim ad minim veniam, quis nostrud</p>
    <span class="stars">★★★★★</span>
    <p class="reviewer">Olive Yew</p>
    <span class="avatar" role="img" aria-label="Client portrait"></span>
  </article>
  <article class="review" style="left:749px">
    <span class="quote">“</span>
    <p class="review-text">Lorem ipsum dolor sit amet, consectetur adipiscing elit, sed do eiusmod tempor incididunt ut labore et dolore magna aliqua. Ut enim ad minim veniam, quis nostrud</p>
    <span class="stars">★★★★★</span>
    <p class="reviewer">Teri Dactyl</p>
    <span class="avatar" role="img" aria-label="Client portrait"></span>
  </article>

  <a class="btn btn-teal btn-pill" style="left:474px;top:518px;width:194px;height:52px">View All Reviews</a>
</section>

<!-- footer -->
<footer class="section footer">
  <div class="logo"><span class="logo-mark"></span>QMT</div>
  <h3 class="footer-heading" style="left:92px;top:148px">Subscribe Newsletter</h3>
  <p class="footer-note">Enter your email address<br>to subscribe this</p>
  <div class="subscribe"><span>Email Address</span><svg width="18" height="18" viewBox="0 0 24 24"><path fill="#fff" d="M2 21 23 12 2 3v7l15 2-15 2z"/></svg></div>

  <h3 class="footer-heading" style="left:460px;top:64px">Quick Link</h3>
  <ul class="links quick" style="left:464px;top:110px"><li>Home</li><li>About</li><li>Services</li><li>Mission</li><li>Resources</li><li>Contact</li></ul>

  <h3 class="footer-heading" style="left:629px;top:64px">Help Links</h3>
  <ul class="links help" style="left:633px;top:110px"><li>Terms &amp; Conditions</li><li>Privacy Policy</li><li>About Us</li><li>Support</li></ul>

  <h3 class="footer-heading" style="left:841px;top:60px">Our Location</h3>
  <div class="contact-item" style="top:108px"><span class="ring"><svg width="14" height="14" viewBox="0 0 24 24"><path fill="none" stroke="#fff" stroke-width="2" d="M12 22s7-7 7-12a7 7 0 0 0-14 0c0 5 7 12 7 12z"/><circle cx="12" cy="10" r="2.5" fill="#fff"/></svg></span><span>61 Lorem ipsum dolor sit<br>amet, consectetur</span></div>
  <div class="contact-item" style="top:168px"><span class="ring"><svg width="14" height="14" viewBox="0 0 24 24"><path fill="#fff" d="M6.6 10.8a15 15 0 0 0 6.6 6.6l2.2-2.2c.3-.3.7-.4 1-.2 1.1.4 2.3.6 3.6.6.6 0 1 .4 1 1V20c0 .6-.4 1-1 1A17 17 0 0 1 3 4c0-.6.4-1 1-1h3.5c.6 0 1 .4 1 1 0 1.3.2 2.5.6 3.6.1.3 0 .7-.2 1z"/></svg></span><span>+1 555-014-2290</span></div>
  <div class="contact-item" style="top:225px"><span class="ring"><svg width="14" height="14" viewBox="0 0 24 24"><rect x="3" y="5" width="18" height="14" rx="2" fill="none" stroke="#fff" stroke-width="2"/><path d="m3 7 9 6 9-6" fill="none" stroke="#fff" stroke-width="2"/></svg></span><span style="font-size:15px">info@qmt-care.com</span></div>

  <div class="rule"></div>
  <p class="copyright">© copyrights 2022 QMT | All Rights Reserved</p>
</footer>

</body>
</html>
```